I need a design with just the number 24. must be in blue color (royal blue) should be large enough for people see must be in the center of page. Place a nice border around the page.

• Number 24 in Royal blue color

```html
<!DOCTYPE html>
<html lang="en">
<head>
<meta charset="UTF-8">
<title>24</title>
<link rel="stylesheet" href="https://fonts.googleapis.com/css2?family=Archivo:ital,wght@1,900&display=swap">
<style>
  :root {
    --paper: #ffffff;
    --royal-blue: #2d3494;
    --gold: #d4a76a;
    --gold-soft: rgba(212, 167, 106, 0.18);
  }
  html, body {
    margin: 0;
    padding: 0;
    overflow: hidden;
    background: var(--paper);
  }
  .page {
    position: relative;
    width: 927px;
    height: 1200px;
    background: var(--paper);
    overflow: hidden;
  }
  .page-frame {
    position: absolute;
    inset: 0;
    width: 927px;
    height: 1200px;
  }
  .page-frame line,
  .page-frame polyline {
    fill: none;
    stroke: var(--gold);
    stroke-width: 1.3;
  }
  .corner-accent {
    position: absolute;
    width: 122px;
    height: 123px;
    background: linear-gradient(135deg, var(--gold-soft), rgba(212, 167, 106, 0.05));
  }
  .corner-accent--top-left {
    left: 68px;
    top: 68px;
  }
  .corner-accent--bottom-right {
    left: 732px;
    top: 1001px;
    background: linear-gradient(315deg, var(--gold-soft), rgba(212, 167, 106, 0.05));
  }
  .big-number {
    position: absolute;
    left: 0;
    right: 0;
    top: 388px;
    text-align: center;
    font-family: "Archivo", "Helvetica Neue", Arial, sans-serif;
    font-style: italic;
    font-weight: 900;
    font-size: 372px;
    line-height: 1;
    letter-spacing: 4px;
    color: var(--royal-blue);
    transform: translateX(-10px);
  }
</style>
</head>
<body>
  <main class="page">
    <svg class="page-frame" viewBox="0 0 927 1200" aria-hidden="true">
      <!-- top rules -->
      <line x1="214" y1="67.5" x2="853" y2="67.5"/>
      <line x1="218" y1="71.5" x2="857" y2="71.5"/>
      <!-- right rules -->
      <line x1="853" y1="67.5" x2="853" y2="994"/>
      <line x1="857" y1="71.5" x2="857" y2="998"/>
      <!-- left rules -->
      <line x1="68" y1="209" x2="68" y2="1121"/>
      <line x1="71.5" y1="213" x2="71.5" y2="1124.5"/>
      <!-- bottom rules -->
      <line x1="68" y1="1121" x2="706" y2="1121"/>
      <line x1="71.5" y1="1124.5" x2="710" y2="1124.5"/>
    </svg>
    <div class="corner-accent corner-accent--top-left" role="img" aria-label="Gold geometric line ornament in the top-left corner"></div>
    <div class="corner-accent corner-accent--bottom-right" role="img" aria-label="Gold geometric line ornament in the bottom-right corner"></div>
    <div class="big-number">24</div>
  </main>
</body>
</html>
```